Business card for a plastic surgeon

i need a business card for a plastic surgeon. I have two adresses. The card should communicate safety, simmetry, beauty and with soft colors.
What i want in the card:
- my logo: Letters "R"and "B" (picture uploaded)
- my name: Renato Bastiani
- my registration: CRM 507 219
- my adresses and phone numbers (2):
- Av Dr Teixeira Lopes, 2710, sala 305 - Vila Olímpia | São Paulo/ SP - Phone: 11 4172-5036
- Al. Itapeva, 47, 3 andar - Alphaville | Barueri/ SP - Phone: 11 6350-2481

- my social network: site, facebook and instagram

Target Market(s)

people (95% girls and women) that want cosmetic procedures and plastic surgery

Industry/Entity Type

Business

Contact Information for Business Card

The card should communicate safety, simmetry, beauty and with soft colors.
Beige, brown, gray, rosy are some options. Color is free

Font styles to use
Serif

Requirements
Must have
• - my logo: Letters "R"and "B" (picture uploaded)
• - my name: Renato Bastiani
• - my registration: CRM 507 219
• - my adresses and phone numbers (2):
• - Av Dr Teixeira Lopes, 2710, sala 305 - Vila Olímpia | São Paulo/ SP - Phone: 11 4172-5036
• - Al. Itapeva, 47, 3 andar - Alphaville | Barueri/ SP - Phone: 11 6350-2481
• - my social network: site, facebook and instagram
Should not have
• other images (only my logo)

```html
<!DOCTYPE html>
<html lang="pt">
<head>
<meta charset="utf-8">
<title>Dr. Renato Bastiani — Cartão de Visita</title>
<link rel="stylesheet" href="https://fonts.googleapis.com/css2?family=Marcellus&family=Tinos&family=Arimo&display=swap">
<style>
  :root {
    --cream: #efe5c5;
    --taupe: #ad8a77;
    --maroon: #5c1a17;
    --ink: #111111;
    --white: #ffffff;
    --page: #ffffff;
  }
  * { margin: 0; padding: 0; box-sizing: border-box; }
  html, body { width: 1200px; height: 982px; overflow: hidden; background: var(--page); }
  .canvas { position: relative; width: 1200px; height: 982px; }
  .card {
    position: absolute; left: 273px; width: 629px; height: 361px;
    overflow: hidden; background: var(--cream);
  }
  .card--front { top: 76px; }
  .card--back { top: 516px; }
  .card__shapes { position: absolute; inset: 0; width: 629px; height: 361px; }
  .monogram {
    position: absolute; font-family: "Marcellus", serif; line-height: 1;
    transform: translateX(-50%); letter-spacing: 2px;
  }
  .card--front .monogram { left: 324px; top: 48px; font-size: 54px; color: var(--ink); }
  .card--back .monogram { left: 312px; top: 126px; font-size: 84px; color: var(--cream); }
  .identity {
    position: absolute; left: 0; right: 0; top: 172px; text-align: center;
    color: var(--white); font-family: "Marcellus", serif;
  }
  .identity__name { font-size: 23px; letter-spacing: 0.5px; font-weight: 400; padding-left: 30px; }
  .identity__role { margin-top: 4px; font-size: 12.5px; letter-spacing: 4px; padding-left: 30px; }
  .identity__crm { letter-spacing: 1.5px; font-weight: 700; }
  .address {
    position: absolute; top: 256px; color: var(--white);
    font-family: "Tinos", serif; font-size: 14px; line-height: 18.5px; font-style: normal;
  }
  .address--left { left: 26px; }
  .address--right { left: 454px; }
  .social {
    position: absolute; top: 334px; left: 0; width: 629px; height: 18px;
    font-family: "Arimo", sans-serif; font-size: 14px;
  }
  .social__item { position: absolute; display: flex; align-items: center; gap: 9px; }
  .social__item:nth-child(1) { left: 61px; }
  .social__item:nth-child(2) { left: 242px; }
  .social__item:nth-child(3) { left: 415px; }
  .social__dot { width: 15px; height: 15px; }
  .social__dot--circle { border-radius: 50%; }
  .social__dot--square { border-radius: 2px; }
  .card--front .social { color: var(--white); }
  .card--front .social__dot { background: var(--white); }
  .card--back .social { top: 324px; color: var(--maroon); }
  .card--back .social__dot { background: var(--maroon); }
</style>
</head>
<body>
<main class="canvas">

  <section class="card card--front" aria-label="Frente do cartão">
    <svg class="card__shapes" viewBox="0 0 629 361" aria-hidden="true">
      <ellipse cx="300" cy="412" rx="420" ry="270" fill="var(--taupe)"/>
      <ellipse cx="315" cy="427" rx="400" ry="281" fill="var(--maroon)"/>
    </svg>
    <div class="monogram">RB</div>
    <header class="identity">
      <h1 class="identity__name">DR. RENATO BASTIANI</h1>
      <p class="identity__role">CIRURGIÃO PLÁSTICO <span class="identity__crm">CRM 507 219</span></p>
    </header>
    <address class="address address--left">
      Av Dr Teixeira Lopes, 2710, sala 305<br>
      Vila Olímpia | São Paulo/ SP<br>
      Phone: 11 4172-5036
    </address>
    <address class="address address--right">
      Al. Itapeva, 47, 3 andar<br>
      Alphaville | Barueri/ SP<br>
      Phone: 11 6350-2481
    </address>
    <ul class="social" style="list-style:none">
      <li class="social__item"><span class="social__dot social__dot--circle"></span>www.yoursite.com</li>
      <li class="social__item"><span class="social__dot social__dot--square"></span>facebook-account</li>
      <li class="social__item"><span class="social__dot social__dot--square"></span>instagram_account</li>
    </ul>
  </section>

  <section class="card card--back" aria-label="Verso do cartão">
    <svg class="card__shapes" viewBox="0 0 629 361" aria-hidden="true">
      <ellipse cx="335" cy="0" rx="410" ry="314" fill="var(--taupe)"/>
      <ellipse cx="315" cy="0" rx="380" ry="310" fill="var(--maroon)"/>
    </svg>
    <div class="monogram">RB</div>
    <ul class="social" style="list-style:none">
      <li class="social__item"><span class="social__dot social__dot--circle"></span>www.yoursite.com</li>
      <li class="social__item"><span class="social__dot social__dot--square"></span>facebook-account</li>
      <li class="social__item"><span class="social__dot social__dot--square"></span>instagram_account</li>
    </ul>
  </section>

</main>
</body>
</html>
```